Letterhead for clinic notes, test reports, and business cards

I need business card and letterheads for a medical clinic with the following:
1- Business cards. The back should allow for space for date and time of next appointments (few lines would do)
2- Letterhead for clinic notes
3- Letterhead for test reports.

Feel free to use whats included for examples. I value creativity so be creative.

Target Market(s)

Patients, referring physicians.

Industry/Entity Type

Health Care

Requirements
Must have
• Must use current logo.
• Must look good on white background
• Letterhead and reports must look good faxed.
• Please use themes of the current logo. Another possible color to use is grey as well (www.brackenvale-cardio.org - use the font color in the text of that website)

```html
<!DOCTYPE html>
<html lang="en">
<head>
<meta charset="utf-8">
<title>Brackenvale Heart Institute – Stationery</title>
<link href="https://fonts.googleapis.com/css2?family=Arimo:ital,wght@0,400;0,700;1,400;1,700&display=swap" rel="stylesheet">
<style>
:root{
  --backdrop:#a7a6a7;
  --paper:#f4f3f2;
  --brand-blue:#1f4f8f;
  --brand-navy:#16256b;
  --brand-red:#b8202a;
  --ink:#222;
  --grey:#555;
  --rule:#888;
}
*{margin:0;padding:0;box-sizing:border-box}
html,body{width:1200px;height:542px;overflow:hidden;background:var(--backdrop);font-family:Arimo,Arial,sans-serif;color:var(--ink)}
.canvas{position:relative;width:1200px;height:542px}
.sheet{position:absolute;background:var(--paper);box-shadow:0 1px 4px rgba(0,0,0,.25)}
.caption{position:absolute;font-size:8px;color:#222;text-align:center}
.wordmark{display:flex;align-items:center;gap:5px;color:var(--brand-blue);font-weight:700;line-height:1.05;font-size:11px;text-transform:uppercase;letter-spacing:.3px}
.wordmark .dot{width:14px;height:14px;border-radius:50%;background:var(--brand-red);flex:none}
.wordmark small{display:block;font-size:8px}

/* clinical letterhead */
.letter{left:33px;top:24px;width:348px;height:491px}
.letter .wordmark{position:absolute;left:27px;top:36px}
.letter-body{position:absolute;left:27px;top:131px;width:295px;font-size:6.4px;line-height:8px}
.letter-body p{margin-bottom:8px}
.letter-footer{position:absolute;left:27px;right:28px;top:442px;border-top:1px solid var(--brand-blue);padding-top:6px;display:flex;justify-content:space-between;font-size:5.6px;line-height:8px;color:var(--grey)}
.letter-footer .web b{color:var(--brand-blue);font-weight:400}
.icon{display:inline-block;width:6px;height:6px;vertical-align:-1px;margin-right:2px}

/* test report */
.report{left:403px;top:24px;width:349px;height:491px}
.report .wordmark{position:absolute;left:27px;top:46px}
.report-contact{position:absolute;right:27px;top:24px;text-align:right;font-size:5.6px;line-height:9px;color:var(--grey)}
.report-contact .web{color:var(--brand-blue)}
.patient{position:absolute;left:27px;top:116px;width:296px;font-size:4.6px;line-height:6px}
.patient .row{display:flex}
.patient .c1{width:102px}
.patient b{font-weight:700}
.patient .big{font-size:5.8px}
.divider{position:absolute;left:27px;width:296px;border-top:.6px solid var(--rule)}
.survey-title{position:absolute;left:0;width:349px;top:186px;text-align:center;font-size:7px;font-weight:700;font-style:italic}
.survey{position:absolute;left:73px;top:199px;border-collapse:collapse;font-size:3.6px;line-height:4.6px;background:#fff}
.survey td,.survey th{border:.4px solid #999;padding:0 2px;font-weight:400;text-align:right}
.survey td:first-child{text-align:left}
.box{display:inline-block;width:3px;height:3px;border:.4px solid #777;margin-right:3px;vertical-align:-.5px}
.report-text{position:absolute;left:27px;width:296px;font-size:4.6px;line-height:6px}
.report-text em{color:var(--brand-red);font-weight:700}
.signature{position:absolute;left:27px;top:366px;width:80px;height:16px;background:linear-gradient(90deg,#e8e7e6,#d4d3d2)}
.sign-block{position:absolute;top:384px;font-size:4.4px;line-height:5.6px;font-style:italic;font-weight:700}

/* business cards */
.card{top:146px;width:152px;height:88px}
.card-front{left:800px;background:linear-gradient(160deg,#1d3f9a,var(--brand-navy));overflow:hidden}
.card-front .ribbon{position:absolute;left:0;top:0}
.card-front .wordmark{position:absolute;left:100px;top:22px;font-size:6px;color:#fff;gap:3px}
.card-front .wordmark small{font-size:4.5px}
.card-front .wordmark .dot{width:7px;height:7px}
.person{position:absolute;left:8px;top:36px;color:#fff;font-size:3.8px;line-height:5px}
.person .name{font-size:6px;line-height:7px}
.card-back{left:968px;background:#fff;padding:8px 8px}
.card-back h3{font-size:6px;font-weight:400;color:var(--brand-blue);text-align:right;margin-bottom:6px}
.field{font-size:3.8px;color:var(--grey);border-bottom:.4px solid #ccc;height:9px;line-height:9px}
.days{display:flex;gap:5px;font-size:3.6px;color:var(--grey);margin:4px 0}
.card-back .note{font-size:3px;font-style:italic;color:#777;text-align:right;margin-top:7px;line-height:4px}

/* envelope */
.envelope{left:774px;top:272px;width:392px;height:244px;background:var(--paper)}
.flap{position:absolute;left:0;top:0}
.flap-web{position:absolute;left:0;width:392px;top:22px;text-align:center;color:#fff;font-size:5.6px;transform:rotate(180deg)}
.envelope .wordmark{position:absolute;left:16px;top:96px}
.envelope .addr{position:absolute;left:34px;top:124px;font-size:6px;line-height:8px;color:var(--grey)}
</style>
</head>
<body>
<div class="canvas">

  <!-- clinical letterhead -->
  <section class="sheet letter">
    <div class="wordmark"><span class="dot"></span><span>Brackenvale Heart<small>Institute</small></span></div>
    <div class="letter-body">
      <p>Date: Month Day, Year</p>
      <p>Address<br>Address<br>Address<br>Address</p>
      <p>Salutation:</p>
      <p>This letter demonstrates the recommended typing format for all correspondence and is an integral part of the letterhead design. The typeface used for body text is the system font for (Macintosh and PC) is Arial Regular 11 pt with 1 pt space leading.</p>
      <p>The body of the letter begins one space below the salutation, using single spacing between lines and double spacing between paragraphs. There are no indentations. The maximum line length should not exceed 6.5 inches. A double space separates the body of the letter from the complimentary close, with at least three spaces to the name of the sender and the title.</p>
      <p style="margin-top:12px">Complimentary close,</p>
      <p style="margin-top:24px">Name of sender<br>Title</p>
      <p>CC/cc</p>
    </div>
    <div class="letter-footer">
      <div>1180 Larkfield Road, Suite 305<br>Brackenvale ON K2P4R8</div>
      <div>
        <svg class="icon" viewBox="0 0 10 10"><path d="M2 1l2 0 1 2-1.2 1a5 5 0 0 0 2.2 2.2L7 5l2 1v2c0 1-1 1-2 1A7 7 0 0 1 1 3c0-1 0-2 1-2z" fill="#1f4f8f"/></svg>555-014-2730<br>
        <svg class="icon" viewBox="0 0 10 10"><rect x="1" y="4" width="8" height="5" fill="#1f4f8f"/><rect x="3" y="1" width="4" height="3" fill="#1f4f8f"/></svg>555-014-2798
      </div>
      <div class="web" style="text-align:right">contact@brackenvale-cardio.org<br><b>www.brackenvale-cardio.org</b></div>
    </div>
  </section>
  <div class="caption" style="left:33px;width:348px;top:524px">Letterhead for Clinical Report</div>

  <!-- test report letterhead -->
  <section class="sheet report">
    <div class="wordmark"><span class="dot"></span><span>Brackenvale Heart<small>Institute</small></span></div>
    <div class="report-contact">
      1180 Larkfield Road, Suite 305<br>Brackenvale ON K2P4R8<br>
      <span style="display:block;margin-top:3px">555-014-2730 ☏</span>
      555-014-2798 ▪<br>contact@brackenvale-cardio.org ✉<br>
      <span class="web">www.brackenvale-cardio.org</span>
    </div>
    <div class="patient">
      <div class="row"><span class="c1"><b>Name</b> &nbsp;&nbsp;&nbsp;&nbsp;&nbsp; <b class="big">Carter, Neil</b></span></div>
      <div class="row"><span class="c1"><b>Exam ID</b> &nbsp;&nbsp; 97329</span><span><b>Med Rec No.</b> &nbsp; 10831159</span></div>
      <div class="row"><span class="c1"><b>Exam Dat</b> &nbsp; 9/8/2010</span><span><b>Date of Birth</b> 4/11/1963 &nbsp; <b>Age</b> 47 &nbsp; <b>Sex</b> Male</span></div>
      <div class="row"><span class="c1">&nbsp;</span><span style="width:96px"><b>Referred By</b> &nbsp; Marlow, Dean</span><span><b>Admission</b> Inpatient</span></div>
      <div class="row"><span class="c1"><b>Risk Factors</b></span><span style="width:110px"><b>V. S. History</b></span><span><b>Room #</b></span></div>
      <div class="row"><span class="c1">Alcohol Abuse</span><span style="width:110px">&nbsp;&nbsp;&nbsp;&nbsp;&nbsp;AAA aneurysm repair</span><span><b>Prior Exam:</b></span></div>
      <div class="row"><span class="c1">CABG</span><span style="width:110px">&nbsp;&nbsp;&nbsp;&nbsp;&nbsp;PTA; renal or visceral</span><span><b>Limited:</b> No</span></div>
      <div class="row"><span class="c1"><b>Medications</b></span><span><b>Reason for Study</b><br>&nbsp;&nbsp;&nbsp;441.3 &nbsp; Abdominal aneurysm -ruptured</span></div>
    </div>
    <div class="divider" style="top:183px"></div>
    <div class="survey-title">Aneurysm Survey</div>
    <table class="survey">
      <tr><th style="text-align:left">Vessel</th><th colspan="3" style="text-align:center">Right</th><th colspan="3" style="text-align:center">Left</th></tr>
      <tr><td></td><td>A-P</td><td>Lat</td><td>Thrombus</td><td>A-P</td><td>Lat</td><td>Thrombus</td></tr>
      <tr><td>Prox CFA</td><td>.95 cm.</td><td>.74 cm.</td><td><span class="box"></span>Present</td><td>cm.</td><td>cm.</td><td><span class="box"></span>Present</td></tr>
      <tr><td>Mid CFA</td><td>.85 cm.</td><td>.95 cm.</td><td><span class="box"></span>Present</td><td>cm.</td><td>cm.</td><td><span class="box"></span>Present</td></tr>
      <tr><td>Distal CFA</td><td>.74 cm.</td><td>.84 cm.</td><td><span class="box"></span>Present</td><td>cm.</td><td>cm.</td><td><span class="box"></span>Present</td></tr>
      <tr><td>Prox SFA</td><td>.87 cm.</td><td>.99 cm.</td><td><span class="box"></span>Present</td><td>cm.</td><td>cm.</td><td><span class="box"></span>Present</td></tr>
      <tr><td>Mid SFA</td><td>2.5 cm.</td><td>2.6 cm.</td><td><span class="box"></span>Present</td><td>cm.</td><td>cm.</td><td><span class="box"></span>Present</td></tr>
      <tr><td>Distal SFA</td><td>.95 cm.</td><td>.94 cm.</td><td><span class="box"></span>Present</td><td>cm.</td><td>cm.</td><td><span class="box"></span>Present</td></tr>
      <tr><td>Prox POP</td><td>.65 cm.</td><td>.54 cm.</td><td><span class="box"></span>Present</td><td>cm.</td><td>cm.</td><td><span class="box"></span>Present</td></tr>
      <tr><td>Mid POP</td><td>.54 cm.</td><td>.54 cm.</td><td><span class="box"></span>Present</td><td>cm.</td><td>cm.</td><td><span class="box"></span>Present</td></tr>
      <tr><td>Distal POP</td><td>.68 cm.</td><td>.68 cm.</td><td><span class="box"></span>Present</td><td>cm.</td><td>cm.</td><td><span class="box"></span>Present</td></tr>
    </table>
    <div class="divider" style="top:272px"></div>
    <div class="report-text" style="top:275px">Noninvasive evaluation of the lower extremity native arteries with B-mode imaging, color Doppler, spectral Doppler analysis and representative diameter measurements.</div>
    <div class="report-text" style="top:292px"><em>Interpretation:</em><br>&nbsp;&nbsp;&nbsp;The maximum diameter measurement of the right superficial femoral artery is 2.6 cm.<br><em>Impression:</em><br>&nbsp;&nbsp;&nbsp;Aneurysm noted on the right superficial femoral artery.</div>
    <div class="signature" role="img" aria-label="Physician's handwritten signature"></div>
    <div class="divider" style="top:383px;width:148px"></div>
    <div class="sign-block" style="left:27px;width:148px;display:flex;justify-content:space-between"><span>Owen R Hale, M.D.</span><span>9/8/2010</span></div>
    <div class="sign-block" style="left:186px;top:375px;font-weight:400">Performed By: &nbsp;&nbsp;&nbsp;<b>Irene Voss, RDMS, RVT</b><br>Transcribed: &nbsp;&nbsp;&nbsp;&nbsp;9/8/2010</div>
    <div class="sign-block" style="left:220px;top:395px;font-weight:400">Report Prepared by VasLine Vascular Database</div>
  </section>
  <div class="caption" style="left:403px;width:349px;top:524px">Letterhead for Test Report</div>

  <!-- business card front -->
  <section class="sheet card card-front">
    <svg class="ribbon" width="152" height="88" viewBox="0 0 152 88" aria-hidden="true">
      <path d="M62 0 Q96 4 96 40 Q96 74 80 88 L152 88 L152 0 Z" fill="#fff"/>
      <path d="M62 0 Q100 2 104 36 Q106 66 86 88 L96 88 Q116 62 112 32 Q106 4 74 0 Z" fill="#b8202a"/>
    </svg>
    <div class="wordmark" style="color:var(--brand-blue)"><span class="dot"></span><span>Brackenvale Heart<small>Institute</small></span></div>
    <div class="person">
      <div class="name">Sam Rowan</div>President<br><br>
      ☏ 555-014-2730<br>▪ 555-014-2798<br>✉ contact@brackenvale-cardio.org<br>www.brackenvale-cardio.org<br>1180 Larkfield Road, Suite 305<br>Brackenvale ON K2P4R8
    </div>
  </section>
  <div class="caption" style="left:800px;width:152px;top:240px;font-size:6px">Front card</div>

  <!-- business card back -->
  <section class="sheet card card-back">
    <h3>Next Appointment</h3>
    <div class="field">Name :</div>
    <div class="field">Date : <span style="margin-left:60px">Time :</span><span style="float:right;font-size:2.8px">AM/PM</span></div>
    <div class="days"><span>Sun <span class="box"></span></span><span>Mon <span class="box"></span></span><span>Tue <span class="box"></span></span><span>Wed <span class="box"></span></span><span>Thu <span class="box"></span></span><span>Fri <span class="box"></span></span><span>Sat <span class="box"></span></span></div>
    <div class="field">Note :</div>
    <div class="note">Please give me 24 hours notice if you are unable to keep your appointment or<br>a cancellation fee may be charged</div>
  </section>
  <div class="caption" style="left:968px;width:152px;top:240px;font-size:6px">Back card</div>

  <!-- envelope -->
  <section class="sheet envelope">
    <svg class="flap" width="392" height="72" viewBox="0 0 392 72" aria-hidden="true">
      <defs><linearGradient id="flapFill" x1="0" y1="0" x2="0" y2="1"><stop offset="0" stop-color="#16256b"/><stop offset="1" stop-color="#2a55b0"/></linearGradient></defs>
      <path d="M0 20 Q0 0 20 0 L372 0 Q392 0 392 20 L392 72 Q196 44 0 72 Z" fill="url(#flapFill)"/>
    </svg>
    <div class="flap-web">www.brackenvale-cardio.org</div>
    <div class="wordmark"><span class="dot"></span><span>Brackenvale Heart<small>Institute</small></span></div>
    <div class="addr">1180 Larkfield Road, Suite 305<br>Brackenvale ON K2P4R8</div>
  </section>
  <div class="caption" style="left:774px;width:392px;top:524px">Envelope</div>

</div>
</body>
</html>
```